Income Tax and Accounting Brochure

I need a brochure using my new logo (file attached). I do tax work and accounting work. I am an EA (QDX Enrolled Agent - logo attached) and would like this incorporated into the brochure. I also have a MSA in Accounting. Please incorporate the text that I have provided in the brochure.

Target Market(s)

Tax Clients - both business and individuals

Industry/Entity Type

Accounting

Colors
0054AA
0677BA
7BADD7
CADEEF
E8F1F8

Requirements
Must have
• Use my logo and the QDX EA file in the brochure
Nice to have
• I would like to see a brochure that I can customize with my own text if possible.

```html
<!DOCTYPE html>
<html lang="en">
<head>
<meta charset="utf-8">
<title>Ridgeline Accounting &amp; Consulting – Tax Brochure</title>
<link href="https://fonts.googleapis.com/css2?family=Open+Sans:wght@300;400;600;700&family=Fira+Sans+Extra+Condensed:wght@500;600;700&family=Ubuntu:wght@300;700&display=swap" rel="stylesheet">
<style>
:root{
  --blue:#1558a8;
  --blue-dark:#0f3f86;
  --red:#c41e36;
  --grey:#c9cacc;
  --grey-mid:#a9aaac;
  --grey-dark:#4a4a4c;
  --paper:#ffffff;
  --backdrop:#e4e5e7;
  --ink:#3a3a3c;
  --ink-soft:#6b6c70;
  --body:'Open Sans',sans-serif;
  --cond:'Fira Sans Extra Condensed',sans-serif;
  --display:'Ubuntu',sans-serif;
}
*{box-sizing:border-box;margin:0;padding:0}
html,body{width:1200px;height:1098px;overflow:hidden;background:var(--backdrop)}
body{position:relative;font-family:var(--body);color:var(--ink)}
.spread{position:absolute;left:227px;width:1105px;height:780px;background:var(--paper);transform:scale(.675);transform-origin:0 0;overflow:hidden}
.spread--outside{top:15px}
.spread--inside{top:556px}
.box{position:absolute}
.spine{position:absolute;top:0;bottom:0;background:var(--grey-mid)}
.photo{position:absolute}

/* outside spread - back panel */
.books-text{position:absolute;left:176px;top:128px;width:320px;font-size:12.6px;line-height:1.3;color:var(--ink)}
.books-text h3{font-family:var(--body);font-weight:700;font-size:17px;color:#111;margin-bottom:1px}
.contact{position:absolute;left:58px;top:655px;font-size:12px;line-height:1.3;color:var(--ink);white-space:nowrap}
.contact .firm{font-family:var(--cond);font-weight:600;font-size:13.5px;color:var(--blue)}
.contact .phone{font-weight:700;font-size:13px;color:#111}
.contact-divider{position:absolute;left:270px;top:660px;width:2px;height:75px;background:var(--grey-mid)}
.email{position:absolute;left:128px;top:737px;font-weight:700;font-size:18px;color:var(--red)}

/* outside spread - front panel */
.brand{position:absolute;left:592px;top:40px;display:flex;align-items:center;gap:14px}
.brand-dot{width:58px;height:58px;border-radius:50%;background:var(--blue)}
.brand-name{font-family:var(--body);font-weight:600;font-size:21px;line-height:1.2;color:var(--blue);letter-spacing:.5px}
.tagline{position:absolute;left:800px;top:170px;width:290px;text-align:center;font-family:var(--body);font-weight:300;font-size:30px;line-height:1.13;color:var(--blue)}
.tagline b{font-weight:700}
.cover-title{position:absolute;left:846px;top:405px;font-family:var(--display);font-weight:700;font-size:37px;line-height:1.05;color:#fff}
.cover-sub{position:absolute;left:888px;top:610px;font-family:var(--body);font-weight:300;font-size:27px;color:#fff}
.quote-mark{position:absolute;font-family:var(--display);font-weight:700;color:var(--red);line-height:1}
.cover-quote{position:absolute;left:640px;top:716px;width:380px;font-family:var(--cond);font-weight:600;font-size:14px;color:var(--blue);white-space:nowrap}

/* inside spread */
.tab-label{position:absolute;left:100px;top:70px;font-family:var(--display);font-weight:700;font-size:30px;color:#fff}
.bio{position:absolute;left:222px;top:507px;width:302px;font-size:12.7px;line-height:1.16;color:var(--ink-soft)}
.bio p+p{margin-top:12px}
.inside-heading{position:absolute;left:591px;top:72px;font-family:var(--cond);font-weight:700;font-size:27px;color:var(--red);white-space:nowrap}
.intro{position:absolute;left:591px;top:112px;width:480px;font-size:12.4px;line-height:1.16;color:var(--ink-soft)}
.intro p+p{margin-top:10px}
.inside-title{position:absolute;left:628px;top:560px;font-family:var(--display);font-weight:700;font-size:33px;line-height:1.02;color:var(--blue)}
.inside-sub{position:absolute;left:628px;top:672px;font-family:var(--body);font-weight:300;font-size:27px;color:var(--blue)}
.benefits-heading{position:absolute;left:828px;top:462px;font-family:var(--cond);font-weight:700;font-size:25px;color:var(--red)}
.benefits{position:absolute;left:830px;top:500px;width:262px;list-style:none;font-size:12.4px;line-height:1.15;color:var(--ink-soft)}
.benefits li{position:relative;padding-left:22px;margin-bottom:7px}
.benefits li::before{content:"";position:absolute;left:0;top:4px;width:8px;height:8px;border-radius:50%;background:var(--blue)}
</style>
</head>
<body>

<section class="spread spread--outside">
  <div class="box" style="left:65px;top:113px;width:13px;height:40px;background:var(--red)"></div>
  <div class="box" style="left:65px;top:153px;width:13px;height:40px;background:var(--grey-dark)"></div>
  <div class="box" style="left:65px;top:193px;width:13px;height:40px;background:var(--blue)"></div>
  <div class="box" style="left:65px;top:233px;width:13px;height:39px;background:var(--grey)"></div>
  <div class="box" style="left:145px;top:113px;width:375px;height:159px;background:var(--grey)"></div>
  <svg class="box" style="left:78px;top:113px" width="88" height="159" viewBox="0 0 88 159"><polygon points="0,0 67,0 67,26 86,44 67,62 67,159 0,159" fill="var(--blue)"/></svg>
  <div class="books-text">
    <h3>Books a Mess: No Problem!</h3>
    If you own a small business and haven't kept up your bookkeeping, don't worry. We can help you. We'll prepare your bookkeeping for the year, prepare a full Schedule C, as well as your personal income tax return. Then we'll help you set up an easy system that allows you to keep your books in tip-top shape next year.
  </div>
  <div class="box" style="left:65px;top:272px;width:80px;height:308px;background:var(--grey-mid)"></div>
  <div class="photo" role="img" aria-label="Calculator, pen and sticky notes on printed financial tables" style="left:145px;top:272px;width:375px;height:308px;background:linear-gradient(150deg,#f2f2f2 0%,#d9d9d9 45%,#eceae6 70%,#cfcfcf 100%)"></div>
  <div class="box" style="left:65px;top:580px;width:112px;height:9px;background:var(--blue)"></div>
  <div class="box" style="left:177px;top:580px;width:112px;height:9px;background:var(--grey-dark)"></div>
  <div class="box" style="left:289px;top:580px;width:112px;height:9px;background:var(--grey-mid)"></div>
  <div class="box" style="left:401px;top:580px;width:114px;height:9px;background:var(--red)"></div>
  <svg class="box" style="left:65px;top:589px" width="450" height="56" viewBox="0 0 450 56"><polygon points="0,0 450,0 450,38 72,38 56,56 40,38 0,38" fill="var(--blue)"/></svg>
  <div class="contact">
    <div class="firm">Ridgeline Accounting &amp; Consulting, LLC</div>
    <div>2280 Meadowbrook Ln, PO Box 14</div>
    <div>Fairhaven, VA 20400</div>
    <div>Fax: (888)555-0142</div>
    <div class="phone">Phone: (540)555-0187</div>
  </div>
  <div class="contact-divider"></div>
  <div class="box" role="img" aria-label="Enrolled agent credential badge" style="left:285px;top:662px;width:215px;height:55px;background:var(--grey);border-radius:3px"></div>
  <div class="email">ridgelineacct@mail.com</div>

  <div class="spine" style="left:520px;width:32px"></div>

  <div class="brand">
    <span class="brand-dot"></span>
    <span class="brand-name">RIDGELINE ACCOUNTING<br>&amp; CONSULTING, LLC</span>
  </div>
  <svg class="box" style="left:552px;top:58px" width="533" height="307" viewBox="0 0 533 307"><polygon points="0,55 345,55 398,2 451,55 533,55 533,307 0,307" fill="var(--grey)"/></svg>
  <div class="tagline">What a joy<br>it is to watch<br><b>success</b> in<br><b>action!</b></div>
  <div class="photo" role="img" aria-label="Hands using a calculator beside printed charts and a tablet" style="left:552px;top:365px;width:276px;height:305px;background:linear-gradient(135deg,#e9edf1 0%,#c6ced6 40%,#9fb7c8 70%,#3d4a55 100%)"></div>
  <div class="box" style="left:828px;top:365px;width:257px;height:305px;background:var(--blue)"></div>
  <div class="cover-title">Tax<br>Preparation</div>
  <div class="cover-sub">– why hire us?</div>
  <div class="box" style="left:1085px;top:0;width:20px;height:365px;background:var(--grey-mid)"></div>
  <div class="box" style="left:1085px;top:365px;width:20px;height:76px;background:var(--red)"></div>
  <div class="box" style="left:1085px;top:441px;width:20px;height:76px;background:var(--grey-dark)"></div>
  <div class="box" style="left:1085px;top:517px;width:20px;height:78px;background:var(--blue)"></div>
  <div class="box" style="left:1085px;top:595px;width:20px;height:75px;background:#eeeeee"></div>
  <div class="box" style="left:1085px;top:670px;width:20px;height:110px;background:var(--grey-mid)"></div>
  <div class="quote-mark" style="left:568px;top:660px;font-size:110px">“</div>
  <div class="cover-quote">Ridgeline Accounting &amp; Consulting, LLC is professional and responsive.</div>
  <div class="quote-mark" style="left:1030px;top:688px;font-size:110px">”</div>
</section>

<section class="spread spread--inside">
  <div class="photo" role="img" aria-label="Faded image of a woman working at a desk with a calculator" style="left:0;top:108px;width:525px;height:377px;background:linear-gradient(120deg,#e6e8ea 0%,#f3f3f3 40%,#dfe2e5 70%,#eef0f2 100%)"></div>
  <div class="photo" role="img" aria-label="Faded world map" style="left:40px;top:485px;width:180px;height:230px;background:linear-gradient(180deg,#f0f6f8 0%,#e6f1f3 60%,#ffffff 100%)"></div>
  <svg class="box" style="left:45px;top:70px" width="206" height="70" viewBox="0 0 206 70"><polygon points="0,0 206,0 206,40 128,40 105,68 82,40 0,40" fill="var(--red)"/></svg>
  <div class="box" style="left:251px;top:70px;width:104px;height:40px;background:var(--grey-dark)"></div>
  <div class="box" style="left:355px;top:70px;width:102px;height:40px;background:var(--blue)"></div>
  <div class="tab-label">About</div>
  <div class="photo" role="img" aria-label="Portrait photo of the firm's accountant" style="left:222px;top:297px;width:168px;height:205px;background:linear-gradient(180deg,#3a3c40 0%,#5b5e64 55%,#7d838c 100%)"></div>
  <div class="quote-mark" style="left:143px;top:480px;font-size:105px">“</div>
  <div class="bio">
    <p>I have a Masters' Degree in accounting and am an QDX Enrolled Agent. I am also a LedgerBooks Advanced Certified Consultant in both the online and desktop products including Enterprise and Point of Sale. I provide individual and small business tax services, Accounting, bookkeeping, QDX representation, insurance audit representation, business license assistance and more.</p>
    <p>I have experience working with a wide variety of clients from the point where they first decide they want to start a business. They are often unsure about what to do first- I have a lot of experience to offer you.</p>
  </div>
  <div class="box" style="left:0;top:730px;width:66px;height:15px;background:var(--red)"></div>
  <div class="box" style="left:66px;top:730px;width:74px;height:15px;background:var(--grey-dark)"></div>
  <div class="box" style="left:140px;top:730px;width:73px;height:15px;background:var(--blue)"></div>
  <div class="box" style="left:213px;top:730px;width:74px;height:15px;background:var(--grey)"></div>

  <div class="spine" style="left:525px;width:53px"></div>

  <div class="inside-heading">What a joy it is to watch success in action!</div>
  <div class="box" style="left:1027px;top:70px;width:78px;height:40px;background:var(--blue)"></div>
  <div class="intro">
    <p>Preparing your own income tax return can be a task that leaves you with more questions than answers. According to a study released by the National Accounting Review Office last year, most taxpayers (77% of 71 million taxpayers) believe they benefited from using a professional tax preparer.</p>
    <p>Whether we like it or not, today's tax laws are so complicated that filing a relatively simple return can be confusing. It is just too easy to overlook deductions and credits to which you are entitled. Even if you use a computer software program there's no substitute for the assistance of an experienced tax professional.</p>
  </div>
  <div class="photo" role="img" aria-label="Faded image of hands reviewing printed charts with a pen" style="left:578px;top:243px;width:527px;height:218px;background:linear-gradient(120deg,#d7dadd 0%,#f1f2f3 35%,#e7eaee 65%,#cfd3d7 100%)"></div>
  <svg class="box" style="left:578px;top:461px" width="70" height="319" viewBox="0 0 70 319"><polygon points="0,0 47,0 47,24 67,44 47,64 47,319 0,319" fill="var(--red)"/></svg>
  <div class="inside-title">Tax<br>Preparation</div>
  <div class="inside-sub">– why hire us?</div>
  <div class="benefits-heading">Here's what your get...</div>
  <ul class="benefits">
    <li>Your tax return will be checked and rechecked by our computer software identifying potential problems the QDX may look at more closely and reviewing the math to limit QDX contacts.</li>
    <li>Your tax return can be filed electronically so you will get a refund back quicker.</li>
    <li>Our staff will show you how to adjust your payroll withholding to get more money back each week. Why give the QDX an interest free loan for up to 16 months.</li>
    <li>We will show you potential deductions to limit your tax liability for next year. In addition, we will give you a sheet of commonly overlooked deductions to limit the following year's tax liability.</li>
  </ul>
</section>

</body>
</html>
```